Meridale Wall Tracking Office

I have a current web site that it looking quite aged and it needs a new lease of life. This is a Graffiti Management Website so is all about data processing and management of information. I want a html 5 view on any platform design. clean crisp and new. I have provided some screen shots of my current site.

Target Market(s)

The Target Market will be local government. most users will not be heavy pc users

Industry/Entity Type

Management

Font styles to use
Sans Serif
Other font styles liked:
• web font like calibri

Colors

Designer to choose colors to be used in the design.

Requirements
Must have
• Must have menus similar to attachments

```html
<!DOCTYPE html>
<html lang="en">
<head>
<meta charset="utf-8">
<title>Meridale Wall Tracking Office</title>
<link rel="stylesheet" href="https://fonts.googleapis.com/css2?family=Open+Sans:wght@400;600&display=swap">
<style>
  :root {
    --green: #8cc63f;
    --ink: #1b1b1b;
    --text: #222222;
    --muted: #888888;
    --white: #ffffff;
    --footer: #111111;
    --hero-dark: #1e1e1e;
    --hero-mid: #5a5a5a;
  }
  * { margin: 0; padding: 0; box-sizing: border-box; }
  html, body { width: 1200px; height: 650px; overflow: hidden; }
  body {
    font-family: "Open Sans", sans-serif;
    background: var(--white);
    color: var(--text);
    position: relative;
  }
  .site-header {
    position: absolute; top: 0; left: 0; width: 1200px; height: 49px;
    background: var(--white);
    border-bottom: 2px solid var(--ink);
  }
  .brand {
    position: absolute; left: 184px; top: 0; width: 158px; height: 49px;
    background: var(--green);
    display: flex; align-items: center; justify-content: center;
    font-size: 24px; font-weight: 600; letter-spacing: 3px;
    color: var(--ink);
  }
  .main-nav {
    position: absolute; left: 404px; top: 0; height: 49px;
    display: flex; align-items: center;
  }
  .main-nav a {
    font-size: 12.5px; font-weight: 600; color: var(--ink);
    text-decoration: none; padding: 0 11px;
    border-left: 1px solid #b5b5b5; line-height: 14px;
  }
  .main-nav a:first-child { border-left: none; }
  .main-nav a.is-active { color: var(--green); }
  .main-nav a.wide { padding: 0 16px; }
  .hero {
    position: absolute; top: 49px; left: 0; width: 1200px; height: 228px;
    background: radial-gradient(ellipse at 55% 110%, #0d0d0d 0%, var(--hero-dark) 35%, var(--hero-mid) 75%, #3a3a3a 100%);
  }
  .hero-title {
    position: absolute; top: 96px; left: 0; width: 1200px;
    text-align: center; color: var(--white);
    font-size: 38px; font-weight: 600; letter-spacing: 0.3px;
    text-shadow: 2px 3px 4px rgba(0,0,0,0.8);
  }
  .features {
    position: absolute; top: 318px; left: 0; width: 1200px;
  }
  .feature {
    position: absolute; top: 0; width: 170px; text-align: center;
  }
  .feature svg { display: block; margin: 0 auto; height: 86px; }
  .feature p {
    margin-top: 33px; font-size: 12.3px; line-height: 15.4px; color: var(--text);
  }
  .site-footer {
    position: absolute; top: 600px; left: 0; width: 1200px; height: 50px;
    background: var(--footer); border-top: 4px solid var(--green);
    display: flex; align-items: center; justify-content: center;
    color: var(--white); font-size: 12.5px;
  }
</style>
</head>
<body>
  <header class="site-header">
    <div class="brand">MWTO</div>
    <nav class="main-nav">
      <a class="is-active" href="#">USER HOME</a>
      <a href="#">ADD A JOB</a>
      <a href="#">CURRENT JOBS</a>
      <a href="#">SEARCH JOBS</a>
      <a class="wide" href="#">REPORTS</a>
      <a class="wide" href="#">USER DETAILS</a>
      <a href="#">ADMIN</a>
    </nav>
  </header>

  <section class="hero" role="img" aria-label="Black and white photograph of an artist painting a large mural wall">
    <h1 class="hero-title">HELPING YOU CLEAN UP YOUR COMMUNITY</h1>
  </section>

  <section class="features">
    <div class="feature" style="left:195px">
      <svg viewBox="0 0 90 86" aria-hidden="true">
        <circle cx="30" cy="24" r="14" fill="var(--green)"/>
        <circle cx="30" cy="24" r="17" fill="none" stroke="var(--green)" stroke-width="7" stroke-dasharray="5 5.7"/>
        <circle cx="30" cy="24" r="6" fill="var(--white)"/>
        <circle cx="62" cy="46" r="12" fill="var(--ink)"/>
        <circle cx="62" cy="46" r="15" fill="none" stroke="var(--ink)" stroke-width="6" stroke-dasharray="4.5 4.9"/>
        <circle cx="62" cy="46" r="5" fill="var(--white)"/>
        <circle cx="28" cy="66" r="10" fill="var(--ink)"/>
        <circle cx="28" cy="66" r="12" fill="none" stroke="var(--ink)" stroke-width="5" stroke-dasharray="3.8 3.8"/>
        <circle cx="28" cy="66" r="4" fill="var(--white)"/>
      </svg>
      <p>MWTO is an Online Database System to Manage Graffiti in your area or Your Properties. MWTO allows you to Register, Track, Report and Archive Graffiti Jobs with Photographic Records.</p>
    </div>
    <div class="feature" style="left:406px">
      <svg viewBox="0 0 90 86" aria-hidden="true">
        <path d="M22 6 L80 12 L74 62" fill="none" stroke="var(--ink)" stroke-width="6"/>
        <rect x="12" y="16" width="56" height="58" fill="var(--ink)"/>
        <rect x="20" y="24" width="40" height="42" fill="var(--white)"/>
        <line x1="32" y1="45" x2="48" y2="36" stroke="var(--green)" stroke-width="3"/>
        <line x1="32" y1="45" x2="48" y2="54" stroke="var(--green)" stroke-width="3"/>
        <circle cx="31" cy="45" r="5" fill="var(--green)"/>
        <circle cx="49" cy="35" r="5" fill="var(--green)"/>
        <circle cx="49" cy="55" r="5" fill="var(--green)"/>
      </svg>
      <p>MWTO records both Estimated and Actual hours and costs for each job, enabling you to track the effectiveness of Anti Graffiti policy.</p>
    </div>
    <div class="feature" style="left:614px">
      <svg viewBox="0 0 90 86" aria-hidden="true">
        <path d="M14 4 H50 L64 18 V82 H14 Z" fill="none" stroke="var(--ink)" stroke-width="5"/>
        <line x1="22" y1="24" x2="46" y2="24" stroke="var(--ink)" stroke-width="4"/>
        <line x1="22" y1="34" x2="52" y2="34" stroke="var(--ink)" stroke-width="4"/>
        <line x1="22" y1="44" x2="48" y2="44" stroke="var(--ink)" stroke-width="4"/>
        <line x1="22" y1="54" x2="40" y2="54" stroke="var(--ink)" stroke-width="4"/>
        <line x1="22" y1="64" x2="34" y2="64" stroke="var(--ink)" stroke-width="4"/>
        <path d="M46 70 L80 34 L88 42 L54 78 L42 82 Z" fill="var(--green)"/>
      </svg>
      <p>MWTO allows sharing of Critical Graffiti Tag and Photographic Data between its subscribers, assisting with tracking down Serial Graffiti Offenders.</p>
    </div>
    <div class="feature" style="left:823px">
      <svg viewBox="0 0 90 86" aria-hidden="true">
        <rect x="12" y="52" width="11" height="32" fill="var(--ink)"/>
        <rect x="28" y="42" width="11" height="42" fill="var(--ink)"/>
        <rect x="44" y="48" width="11" height="36" fill="var(--ink)"/>
        <rect x="60" y="38" width="11" height="46" fill="var(--ink)"/>
        <rect x="76" y="32" width="11" height="52" fill="var(--ink)"/>
        <polyline points="17,32 34,20 50,24 66,14 82,8" fill="none" stroke="var(--green)" stroke-width="3"/>
        <circle cx="17" cy="32" r="4" fill="var(--green)"/>
        <circle cx="34" cy="20" r="4" fill="var(--green)"/>
        <circle cx="50" cy="24" r="4" fill="var(--green)"/>
        <circle cx="66" cy="14" r="4" fill="var(--green)"/>
        <circle cx="82" cy="8" r="4" fill="var(--green)"/>
      </svg>
      <p>MWTO has a Statistical and Comparison Reporting Systems to allow its subscribers to graphically report and compare their Graffiti Data.</p>
    </div>
  </section>

  <footer class="site-footer">Copyright 2014 MWTO all rights reserved</footer>
</body>
</html>
```